Arranging Your Money Matters PowerPoint

I need to create a PowerPoint presentation that describes our product and demonstrates how to use it. Our product is an organizational binder that helps clients put all of their important financial and legal documents in one place. I will upload all forms that will be in the binder, as well as our logo and the table of contents. Initially, I think it makes sense to have a slide for every section in the table of contents. There are 18 sections, so I would envision approximately 20 slides.
I would like the first slide to have a deep blue background, with the logo in a shiny gold if possible.
At some point in the presentation slides or throughout, I would like to have the WorkLoop logo, and I would like it to have the following contact information:

Deirdre Valcourt
arrangingyourmoneymatters@mailbox-example.net

I have uploaded the forms that will be in the binder, and each file has a number at the beginning of the file name so they are in order of how they go into the binder. The table of contents is the second file, and will give you an idea of some discussion points.

I have uploaded a photo of the front of a binder to give an idea for color of the main slide and logo. However, please note that the NEW logo has been uploaded. The binder in the picture does not have the correct logo.

Target Market(s)

Financial Advisors, Accountants, Attorneys, and clients of them

Industry/Entity Type

Financial Planning

Requirements
Must have
• 1. I think we can condense the Table of Contents onto one slide by just listing the heading for each section (i.e. Survivor Instructions, Important Contacts, etc.) but leaving out the detail for each section. It will not be necessary to have page numbers for the items in the table of contents.
• 2. After the table of contents slide, I would like to have a slide for each section heading, and the detail for each heading on that slide. The slides would be:
• - title slide
• - Opening Letter
• - Table of Contents
• - Survivor Instructions
• - Important Contacts
• - Information Access
• - Asset Statements
• - Loan Statements
• - Household Billing Statements
• - Education Planning
• - Insurance Inventory
• - Estate Planning
• - Powers of Attorney
• - Family Legal
• - Business Formations
• - Healthcare
• - Future Income
• - Taxes
• - Personal History
• - Resources
• - Important Documents
• Each of these slides would have the content listed under that heading in the table of contents.
• The last slide should say something like "Thank You!" and have:
• 1. The Arrange Your Money Matters logo
• 2. The WorkLoop logo
• 3. Deirdre Valcourt
• 4. arrangeyourmoneymatters@mailbox-example.net
Nice to have
• Colorful visuals or graphics
Should not have
• Slides with too much information on them

```html
<!DOCTYPE html>
<html lang="en">
<head>
<meta charset="utf-8">
<title>Arranging Your Money Matters – Presentation Slides</title>
<link rel="stylesheet" href="https://fonts.googleapis.com/css2?family=Libre+Baskerville&family=Open+Sans:wght@300;400;600;700&display=swap">
<style>
  :root{
    --navy:#0e1552;
    --navy-deep:#0a0f42;
    --gold:#c9a63a;
    --gold-light:#e0c468;
    --ink:#3a3a3a;
    --rule:#cfcfcf;
    --white:#ffffff;
  }
  *{box-sizing:border-box;margin:0;padding:0}
  html,body{width:1200px;height:1200px;overflow:hidden;background:var(--white)}
  body{position:relative;font-family:"Open Sans",sans-serif;color:var(--ink)}

  .slide{position:absolute;width:570px;height:321px;overflow:hidden;background:var(--white);box-shadow:0 2px 10px rgba(0,0,0,.12)}
  .slide--title{left:18px;top:58px}
  .slide--contents{left:608px;top:58px}
  .slide--survivor{left:17px;top:444px}
  .slide--access{left:608px;top:444px}
  .slide--thanks{left:323px;top:826px}

  /* Title slide */
  .hero-photo{position:absolute;left:0;top:0;width:100%;height:154px;background:linear-gradient(100deg,#161d5a 0%,#2a3170 45%,#1a2160 70%,#121a55 100%)}
  .hero-mist{position:absolute;left:0;top:154px;width:100%;height:149px;background:linear-gradient(180deg,#f6f7f9 0%,#e9ebef 60%,#dcdfe5 100%)}
  .hero-base{position:absolute;left:0;top:303px;width:100%;height:18px;background:var(--navy)}
  .hero-brand{position:absolute;left:0;top:200px;width:100%;display:flex;align-items:center;justify-content:center;gap:14px}
  .hero-brand__dot{width:22px;height:22px;border-radius:50%;background:var(--navy)}
  .hero-brand__name{font-family:"Libre Baskerville",serif;font-size:28px;color:var(--navy);white-space:nowrap}

  /* Contents slide */
  .slide-heading{position:absolute;font-family:"Libre Baskerville",serif;font-size:17.5px;color:var(--navy)}
  .slide--contents .slide-heading{left:46px;top:24px}
  .toc{position:absolute;top:64px;width:192px;list-style:none}
  .toc--left{left:48px}
  .toc--right{left:264px}
  .toc__item{display:flex;align-items:center;height:17.4px;border-bottom:1px solid #e2e2e2;font-size:10.2px;color:#555;white-space:nowrap}
  .toc__num{flex:none;width:22px;height:14px;margin-right:6px;background:var(--navy);color:var(--white);font-weight:700;font-size:8.5px;display:flex;align-items:center;justify-content:center}
  .contents-band{position:absolute;left:0;top:244px;width:100%;height:78px;background:var(--navy);border-top:1px solid var(--gold)}
  .contents-band__rule{position:absolute;left:0;top:58px;width:100%;height:1px;background:var(--gold)}
  .contents-band__brand{position:absolute;right:24px;top:16px;display:flex;align-items:center;gap:8px}
  .contents-band__name{font-family:"Open Sans",sans-serif;font-size:9px;color:var(--gold)}
  .dot{display:inline-block;border-radius:50%;background:var(--gold)}
  .contents-band__brand .dot{width:12px;height:12px}

  /* Survivor slide */
  .survivor-band{position:absolute;left:0;top:93px;width:195px;height:101px;background:linear-gradient(180deg,#c7a235 0%,#d9b84f 45%,#bf9a2e 100%)}
  .survivor-band__title{position:absolute;left:46px;top:24px;font-family:"Libre Baskerville",serif;font-size:16px;line-height:1.25;color:var(--white)}
  .survivor-floor{position:absolute;left:0;top:242px;width:100%;height:60px;background:#f1f1f2;border-bottom:1px solid #d8d8d8}
  .survivor-ring{position:absolute;left:499px;top:257px;width:46px;height:46px;border:2px solid #d9d9d9;border-radius:50%}
  .letter{position:absolute;left:194px;top:26px;width:194px;height:260px;background:linear-gradient(90deg,#f4f4f5,#ffffff 30%,#fafafa);box-shadow:-2px 2px 6px rgba(0,0,0,.18)}
  .letter__corner{position:absolute}
  .letter__corner--top{right:0;top:0}
  .letter__corner--bottom{left:0;bottom:0}
  .letter__brand{position:absolute;left:20px;top:12px;display:flex;align-items:center;gap:3px}
  .letter__brand .dot{width:6px;height:6px;background:var(--navy)}
  .letter__brand-name{font-family:"Open Sans",sans-serif;font-size:5px;color:var(--navy)}
  .letter__body{position:absolute;left:22px;top:40px;width:152px;font-size:3.6px;line-height:1.45;color:#333}
  .letter__body p{margin-bottom:2.5px}
  .letter__body ul{list-style:none;padding-left:10px;margin-bottom:2.5px}
  .letter__body li::before{content:"• ";}
  .letter__sign{display:block;width:48px;border-bottom:.5px solid #333;margin:3px 0 1px}

  /* Information access slide */
  .access-photo{position:absolute;left:0;top:120px;width:100%;height:201px;background:linear-gradient(180deg,#ffffff 0%,#eef0f4 45%,#e2e5ec 100%)}
  .slide--access .slide-heading{left:47px;top:22px}
  .access-key{position:absolute;left:49px;top:63px;width:42px;height:42px;border-radius:50%;background:var(--gold)}
  .access-icon{position:absolute;left:69px;width:22px;height:22px;border-radius:50%;background:var(--gold)}
  .access-icon svg,.access-key svg{position:absolute;left:0;top:0}
  .access-table{position:absolute;left:90px;top:75px;width:404px;border-collapse:collapse;font-size:6.4px;color:#222}
  .access-table th{height:17px;background:var(--gold);color:var(--white);font-weight:600;font-size:7px;text-align:center}
  .access-table th:first-child{text-align:left;padding-left:12px}
  .access-table td{height:14.1px;border-bottom:1px solid var(--rule);text-align:center;background:rgba(255,255,255,.7)}
  .access-table td.access-table__title{background:var(--gold);color:var(--white);font-weight:700;text-align:left;padding-left:12px;width:107px;border-bottom:1px solid var(--white)}

  /* Thank-you slide */
  .slide--thanks{background:radial-gradient(circle at 50% 48%,#1b2a6a 0%,#111a55 35%,#0a0f42 75%)}
  .thanks__text{position:absolute;left:0;top:134px;width:100%;text-align:center;font-family:"Open Sans",sans-serif;font-size:29px;color:var(--white)}
</style>
</head>
<body>

<section class="slide slide--title">
  <div class="hero-photo" role="img" aria-label="Photo of a smiling family outdoors, tinted deep blue"></div>
  <div class="hero-mist" role="img" aria-label="Soft white grass and sky photo backdrop"></div>
  <div class="hero-base"></div>
  <div class="hero-brand"><span class="hero-brand__dot"></span><h1 class="hero-brand__name">Arranging Your Money Matters</h1></div>
</section>

<section class="slide slide--contents">
  <h2 class="slide-heading">Table of Contents</h2>
  <ol class="toc toc--left">
    <li class="toc__item"><span class="toc__num">1</span>Survivor Instructions</li>
    <li class="toc__item"><span class="toc__num">2</span>Important Contacts</li>
    <li class="toc__item"><span class="toc__num">3</span>Information Access</li>
    <li class="toc__item"><span class="toc__num">4</span>Asset Statements</li>
    <li class="toc__item"><span class="toc__num">5</span>Loan Statements</li>
    <li class="toc__item"><span class="toc__num">6</span>Household Billing Statements</li>
    <li class="toc__item"><span class="toc__num">7</span>Education Planning</li>
    <li class="toc__item"><span class="toc__num">8</span>Insurance Inventory</li>
    <li class="toc__item" style="border-bottom:none"><span class="toc__num">9</span>Estate Planning</li>
  </ol>
  <ol class="toc toc--right">
    <li class="toc__item"><span class="toc__num">10</span>Powers of Attorney</li>
    <li class="toc__item"><span class="toc__num">11</span>Family Legal</li>
    <li class="toc__item"><span class="toc__num">12</span>Business Formations</li>
    <li class="toc__item"><span class="toc__num">13</span>Healthcare</li>
    <li class="toc__item"><span class="toc__num">14</span>Future Income</li>
    <li class="toc__item"><span class="toc__num">15</span>Taxes</li>
    <li class="toc__item"><span class="toc__num">16</span>Personal History</li>
    <li class="toc__item"><span class="toc__num">17</span>Resources</li>
    <li class="toc__item" style="border-bottom:none"><span class="toc__num">18</span>Important Documents</li>
  </ol>
  <div class="contents-band">
    <div class="contents-band__rule"></div>
    <div class="contents-band__brand"><span class="dot"></span><span class="contents-band__name">Arranging Your Money Matters</span></div>
  </div>
</section>

<section class="slide slide--survivor">
  <div class="survivor-floor"></div>
  <div class="survivor-band" role="img" aria-label="Brushed gold texture band">
    <h2 class="survivor-band__title">Survivor<br>Instructions</h2>
  </div>
  <div class="survivor-ring"></div>
  <article class="letter">
    <svg class="letter__corner letter__corner--top" width="124" height="22" viewBox="0 0 124 22">
      <polygon points="16,0 40,0 18,22 0,22" fill="#0e1552"/>
      <polygon points="46,0 124,0 124,22 26,22" fill="#0e1552"/>
      <polygon points="40,0 46,0 26,22 20,22" fill="#ffffff"/>
    </svg>
    <svg class="letter__corner letter__corner--bottom" width="124" height="20" viewBox="0 0 124 20">
      <polygon points="0,8 90,8 80,20 0,20" fill="#0e1552"/>
      <polygon points="100,0 124,20 84,20" fill="#0e1552"/>
    </svg>
    <div class="letter__brand"><span class="dot"></span><span class="letter__brand-name">Arranging Your Money Matters</span></div>
    <div class="letter__body">
      <p>Dear Friends,</p>
      <p>This binder is one way to simplify and organize your financial and legal papers. It will help your family if you are ever unable to act, and it brings peace of mind during a hard time.</p>
      <p>I suggest the following review schedule:</p>
      <p>February 1 annually:</p>
      <ul><li>Update all account statements</li><li>Update all loan statements</li><li>Update household billing statements</li><li>Review each section for changes</li></ul>
      <p>June 1 annually:</p>
      <ul><li>Update Social Security statements</li><li>Update tax returns</li></ul>
      <p>December 1, every three years:</p>
      <ul><li>Review estate plan provisions</li><li>Review beneficiaries</li><li>Review powers of attorney</li><li>Review healthcare directives</li></ul>
      <p>Please let your family or a trusted friend know where this binder is kept.</p>
      <p>My best to you and your family!</p>
      <p>Sincerely,<span class="letter__sign"></span>Deirdre Valcourt</p>
    </div>
  </article>
</section>

<section class="slide slide--access">
  <div class="access-photo" role="img" aria-label="Faint photo of hanging keys on a light background"></div>
  <h2 class="slide-heading">Information Access</h2>
  <table class="access-table">
    <thead><tr><th>Title</th><th>Location</th><th>Password</th><th>Details</th></tr></thead>
    <tbody>
      <tr><td class="access-table__title">Keypad Lock</td><td>Front Door</td><td>1234</td><td>9v battery</td></tr>
      <tr><td class="access-table__title">Keypad Lock</td><td>Garage Service Door</td><td>5678</td><td>9v battery</td></tr>
      <tr><td class="access-table__title">Keypad Lock</td><td>Dad’s Office Door</td><td>3456</td><td>9v battery</td></tr>
      <tr><td class="access-table__title">Gun Safe</td><td>Dad’s Office</td><td>1357</td><td>2AA batteries</td></tr>
      <tr><td class="access-table__title">Document Safe</td><td>Behind the Old Portrait</td><td>2468</td><td>-</td></tr>
      <tr><td class="access-table__title">Password Manager</td><td>KeyVault on Laptop</td><td>PswrD</td><td>-</td></tr>
      <tr><td class="access-table__title">Dad’s Fonely</td><td>Lock Screen</td><td>0000</td><td>-</td></tr>
      <tr><td class="access-table__title">Combination Lock</td><td>Shed Door</td><td>14-28-24</td><td>SlickSpray helps!</td></tr>
      <tr><td class="access-table__title">Pickup Truck</td><td>Driver’s Door</td><td>3673</td><td>-</td></tr>
      <tr><td class="access-table__title">Voicemail</td><td>Call Home Phone</td><td>1111</td><td>-</td></tr>
      <tr><td class="access-table__title">Mom’s Fonely</td><td>Lock Screen</td><td>9999</td><td>-</td></tr>
      <tr><td class="access-table__title">Notebook Pro</td><td>Lock Screen</td><td>124578</td><td>-</td></tr>
    </tbody>
  </table>
  <div class="access-key">
    <svg width="42" height="42" viewBox="0 0 42 42"><circle cx="14" cy="21" r="4" fill="none" stroke="#fff" stroke-width="2"/><path d="M18 21h14M28 21v4M31 21v3" stroke="#fff" stroke-width="2" fill="none"/></svg>
  </div>
  <div class="access-icon" style="top:118px">
    <svg width="22" height="22" viewBox="0 0 22 22"><rect x="6" y="5" width="10" height="12" fill="none" stroke="#fff" stroke-width="1.2"/><path d="M8.5 8h1M12.5 8h1M8.5 11h1M12.5 11h1M8.5 14h1M12.5 14h1" stroke="#fff" stroke-width="1.2"/></svg>
  </div>
  <div class="access-icon" style="top:175px">
    <svg width="22" height="22" viewBox="0 0 22 22"><rect x="7.5" y="4.5" width="7" height="13" rx="1.2" fill="none" stroke="#fff" stroke-width="1.2"/><circle cx="11" cy="15.5" r=".7" fill="#fff"/></svg>
  </div>
  <div class="access-icon" style="top:243px">
    <svg width="22" height="22" viewBox="0 0 22 22"><rect x="6" y="6" width="10" height="7" fill="none" stroke="#fff" stroke-width="1.2"/><path d="M4 15.5h14" stroke="#fff" stroke-width="1.5"/></svg>
  </div>
</section>

<section class="slide slide--thanks">
  <p class="thanks__text">Thank you!</p>
</section>

</body>
</html>
```